Wedding Brochure/Booklet for Fern & The Hare

We have the content and a previous attempt already. We just need some edits and then have a version we can email as a PDF and Print as a Booklet.

Any further improvements to the visual aspect would also be welcomed

Check out our website to see who we are www.fernandthehare.example

Target Market(s)

Couples!!!!

Industry/Entity Type

Wedding

Font styles to use
Sans Serif
Decorative
Script

Requirements
Must have
• Style
Nice to have
• Style & Elegance
Should not have
• Too bold or Bright Colours

```html
<!DOCTYPE html>
<html lang="en">
<head>
<meta charset="utf-8">
<title>Fern &amp; The Hare – Wedding Booklet Spread</title>
<link rel="stylesheet" href="https://fonts.googleapis.com/css2?family=Didact+Gothic&display=swap">
<style>
  :root {
    --backdrop: #e9e6e3;
    --paper: #ffffff;
    --ink: #2a2a2a;
    --ink-soft: #3a3a3a;
    --blush: #f4c4c4;
    --blush-light: #fbe3e3;
    --photo-light: #ededed;
    --photo-mid: #cfcfcf;
    --photo-dark: #8d8d8d;
  }
  * { box-sizing: border-box; margin: 0; padding: 0; }
  html, body {
    width: 1200px; height: 1200px; overflow: hidden;
    background: var(--backdrop);
    font-family: "Didact Gothic", "Century Gothic", sans-serif;
    color: var(--ink);
  }
  .spread {
    position: absolute; left: 40px; top: 204px;
    width: 1120px; height: 792px;
    display: flex;
    box-shadow: 0 6px 24px rgba(0,0,0,.18);
  }
  .page { position: relative; width: 560px; height: 792px; overflow: hidden; }
  .page--menu { background: var(--paper); }
  .page--terms { background: var(--photo-light); }

  .ornament {
    position: absolute;
    background: radial-gradient(ellipse at center, var(--blush) 0%, var(--blush-light) 60%, rgba(255,255,255,0) 75%);
  }
  .ornament--top { left: -40px; top: 4px; width: 200px; height: 402px; }
  .ornament--bottom { left: 400px; top: 382px; width: 200px; height: 407px; }

  .section { position: absolute; text-align: center; }
  .section__title {
    font-size: 17px; letter-spacing: .2px; font-weight: 400; line-height: 1.1;
  }
  .section__note { font-size: 14px; margin-top: 2px; }
  .section__list { list-style: none; margin-top: 16px; }
  .section__list li { font-size: 11.5px; line-height: 18.2px; color: var(--ink-soft); }

  .beverages { left: 150px; width: 400px; top: 124px; }
  .extras { left: 63px; width: 300px; top: 519px; }
  .extras .section__list { margin-top: 18px; }

  .photo {
    position: absolute; inset: 0;
    background:
      radial-gradient(ellipse 170px 230px at 290px 220px, var(--photo-dark) 0%, rgba(141,141,141,0) 100%),
      radial-gradient(ellipse 160px 150px at 440px 660px, #f7f7f7 0%, rgba(247,247,247,0) 100%),
      linear-gradient(160deg, var(--photo-mid) 0%, var(--photo-light) 55%, #dcdcdc 100%);
  }
  .terms {
    position: absolute; left: 33px; width: 490px; top: 248px;
  }
  .terms__title { font-size: 17px; font-weight: 400; text-align: center; margin-bottom: 24px; }
  .terms p {
    font-size: 10.6px; line-height: 13.5px; text-align: justify;
    color: var(--ink); margin-bottom: 20px;
  }
</style>
</head>
<body>
  <main class="spread">
    <section class="page page--menu">
      <div class="ornament ornament--top" role="img" aria-label="Blush pink filigree swirl ornament"></div>
      <div class="ornament ornament--bottom" role="img" aria-label="Blush pink filigree swirl ornament"></div>

      <div class="section beverages">
        <h2 class="section__title">FERN &amp; THE HARE PREMIUM BEVERAGE PACKAGE</h2>
        <p class="section__note">(Additional Charges Apply)</p>
        <ul class="section__list">
          <li>Beer – Hoshiko,</li>
          <li>Redgum Ridge IPA</li>
          <li>Harbourlight Lite</li>
          <li>Cider - Orchardvale</li>
          <li>Red – Tom Ashgrove “Fandango” 2012 Shiraz</li>
          <li>White – Willow Lane Riesling</li>
          <li>Sparkling – Mount Carrow Brut</li>
          <li>Juice, Soft Drinks &amp; Mineral</li>
        </ul>
      </div>

      <div class="section extras">
        <h2 class="section__title">OPTIONAL EXTRAS</h2>
        <ul class="section__list">
          <li>Tea &amp; Coffee Station by Little Kiln</li>
          <li>Lolly Bar</li>
          <li>Lemonade Stand</li>
          <li>Aussie Seafood Station</li>
          <li>Antipasto Grazing Tables</li>
          <li>Marquee Hire</li>
          <li>Room Set Up</li>
        </ul>
      </div>
    </section>

    <section class="page page--terms">
      <div class="photo" role="img" aria-label="Soft black and white photograph of a bride with a floral headband holding a bouquet of white roses"></div>
      <div class="terms">
        <h2 class="terms__title">Terms &amp; Conditions</h2>
        <p>Fern &amp; The Hare operates as Café serving the general public from 8am to 4pm, 7 days a week. Our Minimum Spends information clearly sets out the times our venue is accessible being from 4pm onwards. Where access is required to set and impacts on our ability to service our patrons, Minimums spends will need to be reviewed.</p>
        <p>Where Fern &amp; The Hare is unable to trade due to an event, minimum spends are increased by $4,000 Monday to Friday, $6000 Saturday and Sundays.</p>
        <p>Upon Receiving your Booking Deposit, we offer a 30 minute meeting up to 6 months prior to your event and a 1hour meeting, up to 4 weeks prior to your Wedding Day to finalise your plans. All other correspondence may be done via email and will be responded to in a timely manner.</p>
        <p>Your total package will be inclusive of Set Up &amp; Pack Down of your event. “Set Up” means the allocation of tables, Chairs, Glasses &amp; Crockery. Where Additional equipment &amp; decorative items are required to be placed, a Set Up fee of $800 is applicable</p>
      </div>
    </section>
  </main>
</body>
</html>
```